Design a website for selling rare gemstones and expensive jewelry

I have URL www.kelvadro.com and need to redo the website. The site I want to build will offer rare expensive gemstones called Paraiba Tourmaline. Some of these gemstones cost millions of dollars!
I like the websites below for the example of quality I am looking for:
Www.carrowmotors.com
Www.vance-hollismotorcars.com
Www.Dravo.com
Www.orsette.com
And Henri Castel website.
It must be simple but elegant and very high end.
Also need SEO work and all marketing done for the site.
I like the sun and beach with the palm trees and beautiful model look along with the high end Carrow/ Vance-Hollis feel….
Zumvo “Beautiful Brazilian Beach”…..

```html
<!DOCTYPE html>
<html lang="en">
<head>
<meta charset="utf-8">
<title>Kelvadro — Rare Gemstones &amp; Fine Jewellery</title>
<link rel="stylesheet" href="https://fonts.googleapis.com/css2?family=Poppins:wght@300;400;500;600&family=Heebo:wght@300;400&family=Kaushan+Script&display=swap">
<style>
:root{
  --bg:#000;
  --panel:#0d0f12;
  --panel-line:#1f2a33;
  --accent:#3d8fc6;
  --accent-light:#6fb6e0;
  --heading:#5aa3cf;
  --text:#e9edf0;
  --muted:#a7adb3;
  --star:#f2c94c;
  --gold:#b89a6c;
  --btn:#2a6fae;
}
*{box-sizing:border-box;margin:0;padding:0}
html,body{width:1200px;height:4597px;overflow:hidden;background:var(--bg)}
body{font-family:"Poppins",sans-serif;color:var(--text);position:relative}
.wrap{position:absolute;left:112px;width:975px}

/* header + hero */
.hero{position:absolute;top:0;left:0;width:1200px;height:571px;background:linear-gradient(100deg,#15191d 0%,#2b2f33 45%,#575b60 70%,#2a2d31 100%)}
.hero-photo{position:absolute;left:680px;top:70px;width:440px;height:470px;border-radius:50%;background:radial-gradient(circle at 50% 45%,#c9ced3 0%,#7d8388 35%,rgba(60,64,68,0) 70%)}
.nav{position:absolute;top:16px;left:118px;width:970px;display:flex;align-items:center}
.logo{font-family:"Poppins",sans-serif;font-weight:400;font-size:30px;letter-spacing:1px;color:var(--accent-light)}
.menu{margin-left:auto;display:flex;align-items:center;gap:30px;font-size:13px;font-weight:500}
.menu .active{color:var(--accent-light)}
.login{background:var(--accent);border-radius:12px;padding:3px 12px;font-size:11px}
.menu svg{display:block}
.hero-kicker{position:absolute;left:118px;top:170px;font-family:"Kaushan Script",cursive;font-size:31px}
.hero-title{position:absolute;left:116px;top:228px;font-family:"Poppins",sans-serif;font-weight:600;font-size:58px;letter-spacing:1px;color:var(--accent-light)}
.hero-sub{position:absolute;left:118px;top:320px;font-size:21px;font-weight:500}
.hero-btn{position:absolute;left:118px;top:381px;width:134px;height:37px;background:var(--btn);font-size:15px;font-weight:500;display:flex;align-items:center;justify-content:center}
.hero-arrow{position:absolute;top:268px;color:#aaa;font-size:24px}
.dots{position:absolute;top:535px;left:580px;display:flex;gap:6px}
.dots span{width:8px;height:8px;border-radius:50%;background:#5f7686}
.dots span.on{background:#cfd8de}

/* features */
.features{top:600px;display:flex;justify-content:space-between}
.feature{width:306px;height:210px;border:1px solid var(--panel-line);background:#050607;text-align:center;padding:18px 20px}
.feature svg{margin:0 auto 12px;display:block}
.feature h3{font-size:15px;font-weight:500;color:var(--heading);margin-bottom:10px}
.feature p{font-size:11px;color:var(--muted);line-height:19px}

.section-title{position:absolute;left:0;width:1200px;text-align:center;font-family:"Heebo",sans-serif;font-weight:300;font-size:34px;color:var(--heading)}
.section-title::after{content:"";display:block;width:190px;height:3px;margin:12px auto 0;background:linear-gradient(90deg,transparent,var(--accent),transparent)}

/* categories */
.cat{position:absolute;border:1px solid var(--panel-line);overflow:hidden}
.cat .photo{position:absolute;inset:0}
.cat .label{position:absolute;left:0;right:0;bottom:0;height:54px;background:rgba(0,0,0,.45);padding:6px 14px}
.cat .label b{display:block;font-weight:500;font-size:20px;line-height:24px;letter-spacing:.5px}
.cat .label small{display:block;font-size:12px;line-height:16px;color:#ccc}

/* product cards */
.card{position:absolute;width:224px;height:293px;background:var(--panel);border:1px solid var(--panel-line)}
.card.hl{border-color:#3d5a72}
.card .photo{height:194px;position:relative}
.card .badge{position:absolute;left:2px;top:2px;background:#1f8a5e;color:#fff;font-size:10px;padding:2px 6px}
.card .tools{position:absolute;right:12px;bottom:8px;display:flex;gap:8px}
.card .tools span{width:24px;height:24px;border-radius:50%;background:#fff;display:flex;align-items:center;justify-content:center}
.card .name{text-align:center;font-size:13px;margin-top:14px;white-space:nowrap}
.card .name.blue{color:var(--accent-light)}
.card .stars{text-align:center;color:var(--star);font-size:13px;letter-spacing:3px;margin-top:2px}
.card .price{text-align:center;color:var(--accent-light);font-size:15px;margin-top:4px}
.slide-arrow{position:absolute;top:1938px;width:32px;height:32px;background:#1a1a1a;display:flex;align-items:center;justify-content:center;color:#fff;font-size:14px}

/* banner */
.banner{position:absolute;top:2190px;left:0;width:1200px;height:350px;background:linear-gradient(90deg,#2b1c1c 0%,#4a3434 30%,#5a4946 60%,#3d3a3c 100%);text-align:center}
.banner .kicker{margin-top:60px;font-size:17px;font-weight:600}
.banner h2{font-family:"Kaushan Script",cursive;font-weight:400;font-size:44px;color:#e7cfa6;margin-top:6px}
.banner p{width:620px;margin:10px auto 0;font-size:15px;line-height:24px}
.banner .cta{display:inline-block;margin-top:20px;background:var(--gold);padding:9px 26px;font-size:14px;font-weight:500}

.load-more{position:absolute;left:539px;top:3363px;width:122px;height:30px;background:var(--btn);font-size:12px;display:flex;align-items:center;justify-content:center;gap:6px;border:1px solid #4d8fc8}

/* lists */
.lists{top:3506px;display:flex;justify-content:space-between}
.list{width:306px}
.list h4{font-family:"Heebo",sans-serif;font-weight:300;font-size:26px;padding-bottom:6px;border-bottom:2px solid #444;margin-bottom:10px}
.item{display:flex;align-items:center;gap:16px;padding:8px 6px;border-bottom:1px solid #222;height:71px}
.item .thumb{width:56px;height:56px;flex:none}
.item b{display:block;color:var(--accent-light);font-weight:500;font-size:17px}
.item small{font-size:12px}

/* newsletter */
.newsletter{position:absolute;top:3978px;left:0;width:1200px;height:112px;background:#0f1112}
.newsletter .copy{position:absolute;left:112px;top:26px}
.newsletter .copy span{font-size:16px}
.newsletter .copy b{display:block;font-weight:500;font-size:23px;color:var(--heading);letter-spacing:.5px}
.newsletter .field{position:absolute;left:613px;top:34px;width:331px;height:44px;background:#000;padding:12px 18px;font-size:16px}
.newsletter .sub{position:absolute;left:944px;top:34px;width:143px;height:44px;background:var(--accent);font-size:15px;font-weight:500;display:flex;align-items:center;justify-content:center}

/* footer */
.footer{position:absolute;top:4090px;left:0;width:1200px;height:507px;background:#0a0b0c}
.footer .col{position:absolute;top:52px}
.footer h5{font-weight:400;font-size:22px;color:var(--heading);margin-bottom:14px;padding-bottom:4px;border-bottom:1px solid #2a3a46;display:inline-block}
.footer li{list-style:none;font-size:14px;color:#ddd;height:32px}
.footer p{font-size:12px;line-height:20px;width:300px}
.socials{display:flex;gap:10px;margin-top:22px}
.socials span{width:30px;height:30px;border:1px solid #333;display:block}
.bottom{position:absolute;top:350px;left:112px;width:975px;display:flex;font-size:14px}
.bottom .links{margin-left:auto;display:flex;gap:12px}
.bottom .links i{width:1px;background:#888;display:block}
</style>
</head>
<body>

<section class="hero">
  <div class="hero-photo" role="img" aria-label="Silver diamond ring with sweeping bands on a dark backdrop"></div>
  <nav class="nav">
    <div class="logo">KELVADRO</div>
    <div class="menu">
      <span class="active">HOME</span><span>ABOUT</span><span>PRODUCTS ▾</span><span>SHOP</span><span>CONTACT</span>
      <span class="login">LOGIN</span>
      <svg width="20" height="18" viewBox="0 0 24 22"><path d="M12 21 2 11a5.5 5.5 0 0 1 10-7 5.5 5.5 0 0 1 10 7z" fill="#fff"/></svg>
      <svg width="18" height="20" viewBox="0 0 18 20"><path d="M2 6h14l-1 13H3z" fill="#fff"/><path d="M6 6V4a3 3 0 0 1 6 0v2" stroke="#fff" stroke-width="2" fill="none"/></svg>
    </div>
  </nav>
  <div class="hero-kicker">It Has Final Started</div>
  <div class="hero-title">HUGE SELL</div>
  <div class="hero-sub">Up To 70% Off</div>
  <div class="hero-btn">Shop Now ›</div>
  <div class="hero-arrow" style="left:36px">‹</div>
  <div class="hero-arrow" style="left:1150px">›</div>
  <div class="dots"><span></span><span class="on"></span><span></span></div>
</section>

<section class="wrap features">
  <div class="feature">
    <svg width="58" height="46" viewBox="0 0 58 46" fill="none" stroke="#ddd" stroke-width="2"><rect x="4" y="10" width="32" height="22"/><path d="M36 16h10l8 8v8H36"/><circle cx="14" cy="36" r="5"/><circle cx="44" cy="36" r="5"/><text x="9" y="25" font-size="9" fill="#ddd" stroke="none" font-family="Poppins">FREE</text></svg>
    <h3>FREE SHIPPING ON ALL ORDERS</h3>
    <p>Get Free Shipping on all orders over $75 and free returns to our UK returns centre! Items are dispatched from the US and will arrive in 5-8 days.</p>
  </div>
  <div class="feature">
    <svg width="58" height="46" viewBox="0 0 58 46" fill="none" stroke="#ddd" stroke-width="2"><circle cx="29" cy="20" r="14"/><path d="M15 20a14 14 0 0 1 28 0"/><rect x="11" y="18" width="5" height="10"/><rect x="42" y="18" width="5" height="10"/><path d="M14 42c3-6 9-8 15-8s12 2 15 8"/></svg>
    <h3>AMAZING CUSTOMER SERVICE</h3>
    <p>Lorem ipsum dolor sit amet, consectetur adipisicing elit. Nulla veniam illum impedit laboriosam molestias est provident eveniet dicta, alias facere sapiente.</p>
  </div>
  <div class="feature">
    <svg width="58" height="46" viewBox="0 0 58 46" fill="none" stroke="#ddd" stroke-width="2"><rect x="4" y="10" width="32" height="22"/><path d="M36 16h10l8 8v8H36"/><circle cx="14" cy="36" r="5"/><circle cx="44" cy="36" r="5"/><text x="9" y="25" font-size="9" fill="#ddd" stroke="none" font-family="Poppins">FREE</text></svg>
    <h3>NO CUSTOMS OR DUTY FEES!</h3>
    <p>We pay these fees so you don't have to! The total billed at checkout is the final amount you pay, inclusive of VAT, with no additional charges at the time of delivery!</p>
  </div>
</section>

<h2 class="section-title" style="top:896px">BROWSE OUR CATEGORIES</h2>

<div class="cat" style="left:112px;top:1013px;width:474px;height:265px">
  <div class="photo" role="img" aria-label="Diamond necklace and jewellery on dark velvet" style="background:linear-gradient(120deg,#1a1a1f,#6b6a68 45%,#3a2e22)"></div>
  <div class="label"><b>DIAMOND AND JEWELLERY</b><small>5 Products</small></div>
</div>
<div class="cat" style="left:613px;top:1013px;width:474px;height:265px">
  <div class="photo" role="img" aria-label="Charm bracelet with silver and gold beads" style="background:linear-gradient(120deg,#e4e4e6,#b9ad98 45%,#4a4440)"></div>
  <div class="label"><b>BRCELET</b><small>2 Products</small></div>
</div>
<div class="cat" style="left:112px;top:1305px;width:308px;height:265px">
  <div class="photo" role="img" aria-label="Ornate gold and gem necklace" style="background:linear-gradient(140deg,#2a0d0d,#6a3a22 50%,#1a0a06)"></div>
  <div class="label"><b>JEWELLERY</b><small>3 Products</small></div>
</div>
<div class="cat" style="left:445px;top:1305px;width:308px;height:265px">
  <div class="photo" role="img" aria-label="Stacked silver diamond rings" style="background:radial-gradient(circle at 50% 40%,#a9b0b6,#2c3033 55%,#050505)"></div>
  <div class="label"><b>RING</b><small>5 Products</small></div>
</div>
<div class="cat" style="left:780px;top:1305px;width:307px;height:265px">
  <div class="photo" role="img" aria-label="Assorted coloured tourmaline gemstones" style="background:linear-gradient(135deg,#b7b7b9,#9c8f95 50%,#8a8d7a)"></div>
  <div class="label"><b style="text-transform:none">tourmaline</b><small>5 Products</small></div>
</div>

<h2 class="section-title" style="top:1705px">BEST SELLING PRODUCTS</h2>
<div class="slide-arrow" style="left:66px">‹</div>
<div class="slide-arrow" style="left:1102px">›</div>

<div class="card" style="left:112px;top:1821px"><div class="photo" role="img" aria-label="Ruby ring with diamond halo" style="background:radial-gradient(circle at 50% 45%,#7a2a2a,#2a1a14 50%,#0a0a0a)"></div><div class="name">Kelvadro Tourmaline Necklace</div><div class="stars">★★★★★</div><div class="price">$ 1,150.00</div></div>
<div class="card" style="left:363px;top:1821px"><div class="photo" role="img" aria-label="Gold pendant with oval red stone" style="background:radial-gradient(circle at 50% 45%,#8a1a1a,#8c7a52 45%,#1a1a1a)"></div><div class="name">Kelvadro Pendant</div><div class="stars">★★★★★</div><div class="price">$ 1,150.00</div></div>
<div class="card hl" style="left:613px;top:1821px"><div class="photo" role="img" aria-label="Gold ring with red gemstone" style="background:radial-gradient(circle at 50% 40%,#b8481e,#6a4a1a 40%,#050505 75%)"><div class="tools"><span><svg width="12" height="11" viewBox="0 0 24 22"><path d="M12 21 2 11a5.5 5.5 0 0 1 10-7 5.5 5.5 0 0 1 10 7z" fill="#000"/></svg></span><span><svg width="10" height="12" viewBox="0 0 18 20"><path d="M2 6h14l-1 13H3z" fill="#000"/></svg></span></div></div><div class="name">Tourmaline Necklace</div><div class="stars">★★★★★</div><div class="price">$ 2,150.00</div></div>
<div class="card" style="left:863px;top:1821px"><div class="photo" role="img" aria-label="Silver ring with red centre stone" style="background:radial-gradient(circle at 50% 45%,#c6c7c9,#5a5c5e 45%,#111)"></div><div class="name">Kelvadro Necklace</div><div class="stars">★★★★★</div><div class="price">$ 2,000.00</div></div>

<section class="banner" role="img" aria-label="Model wearing jewellery in warm muted tones">
  <div class="kicker">GET SPAECIAL PRICE THIS WEEK</div>
  <h2>Custom Your Jewellery Now</h2>
  <p>Lorem ipsum dolor sit amet, consectetur adipisicing elit. Repudiandae alias, libero. Aspernatur magnam, ipsum nemo ad provident dolorem. Eaque veritatis architecto, nulla delectus eos suscipit ipsam sint veniam libero asperiores?</p>
  <div class="cta">GET STARTED</div>
</section>

<h2 class="section-title" style="top:2600px">Our Products</h2>

<div class="card" style="left:112px;top:2717px"><div class="photo" role="img" aria-label="Ruby ring with diamond halo" style="background:radial-gradient(circle at 50% 45%,#7a2a2a,#2a1a14 50%,#0a0a0a)"><span class="badge">Out Of Stoke</span></div><div class="name">Kelvadro Tourmaline Necklace</div><div class="stars">★★★★★</div><div class="price">$ 1,150.00</div></div>
<div class="card" style="left:363px;top:2717px"><div class="photo" role="img" aria-label="Gold pendant with oval red stone" style="background:radial-gradient(circle at 50% 45%,#8a1a1a,#8c7a52 45%,#1a1a1a)"></div><div class="name">Kelvadro Tourmaline Necklace</div><div class="stars">★★★★★</div><div class="price">$ 1,150.00</div></div>
<div class="card" style="left:613px;top:2717px"><div class="photo" role="img" aria-label="Gold ring with red gemstone" style="background:radial-gradient(circle at 50% 40%,#b8481e,#6a4a1a 40%,#050505 75%)"><span class="badge">10% Off</span><div class="tools"><span><svg width="12" height="11" viewBox="0 0 24 22"><path d="M12 21 2 11a5.5 5.5 0 0 1 10-7 5.5 5.5 0 0 1 10 7z" fill="#000"/></svg></span><span><svg width="10" height="12" viewBox="0 0 18 20"><path d="M2 6h14l-1 13H3z" fill="#000"/></svg></span></div></div><div class="name">Kelvadro Tourmaline Necklace</div><div class="stars">★★★★★</div><div class="price">$ 1,150.00</div></div>
<div class="card" style="left:863px;top:2717px"><div class="photo" role="img" aria-label="Silver ring with red centre stone" style="background:radial-gradient(circle at 50% 45%,#c6c7c9,#5a5c5e 45%,#111)"><span class="badge">Out Of Stoke</span></div><div class="name">Kelvadro Tourmaline Necklace</div><div class="stars">★★★★★</div><div class="price">$ 1,150.00</div></div>

<div class="card" style="left:112px;top:3038px"><div class="photo" role="img" aria-label="Ruby ring on white band" style="background:radial-gradient(circle at 50% 55%,#a11a22,#3a1a1a 35%,#050505 70%)"><span class="badge">Out Of Stoke</span></div><div class="name">Kelvadro Tourmaline Necklace</div><div class="stars">★★★★★</div><div class="price">$ 1,150.00</div></div>
<div class="card" style="left:363px;top:3038px"><div class="photo" role="img" aria-label="Gold chains with turquoise pendants" style="background:linear-gradient(135deg,#6a5a44,#b39c78 45%,#4a6a6a)"></div><div class="name">Kelvadro Tourmaline Necklace</div><div class="stars">★★★★★</div><div class="price">$ 1,150.00</div></div>
<div class="card hl" style="left:613px;top:3038px"><div class="photo" role="img" aria-label="Glass drop earrings with blue stones" style="background:linear-gradient(135deg,#3a2a2a,#5a3a44 45%,#2a6a6a)"><span class="badge">10% Off</span><div class="tools"><span><svg width="12" height="11" viewBox="0 0 24 22"><path d="M12 21 2 11a5.5 5.5 0 0 1 10-7 5.5 5.5 0 0 1 10 7z" fill="#000"/></svg></span><span><svg width="10" height="12" viewBox="0 0 18 20"><path d="M2 6h14l-1 13H3z" fill="#000"/></svg></span></div></div><div class="name blue">Kelvadro Tourmaline Necklace</div><div class="stars">★★★★★</div><div class="price">$ 1,150.00</div></div>
<div class="card" style="left:863px;top:3038px"><div class="photo" role="img" aria-label="Beaded necklace with turquoise bar pendant" style="background:linear-gradient(180deg,#1a1a14,#3a3a2a 50%,#2a8a8a)"></div><div class="name">Kelvadro Tourmaline Necklace</div><div class="stars">★★★★★</div><div class="price">$ 1,150.00</div></div>

<div class="load-more">Load More <svg width="12" height="12" viewBox="0 0 12 12" fill="none" stroke="#fff" stroke-width="1.5"><path d="M10 6a4 4 0 1 1-1.2-2.8M10 1v2.5H7.5"/></svg></div>

<section class="wrap lists">
  <div class="list">
    <h4>LATEST</h4>
    <div class="item"><div class="thumb" role="img" aria-label="Ruby ring" style="background:radial-gradient(#7a2a2a,#111 70%)"></div><div><b>Kelvadro Diamond</b><small>$2,200.00</small></div></div>
    <div class="item"><div class="thumb" role="img" aria-label="Red gemstone ring" style="background:radial-gradient(#a11a22,#111 70%)"></div><div><b>Kelvadro Diamond</b><small>$2,200.00</small></div></div>
    <div class="item"><div class="thumb" role="img" aria-label="Gold ring with red stone" style="background:radial-gradient(#b8481e,#111 70%)"></div><div><b>Kelvadro Diamond</b><small>$2,200.00</small></div></div>
    <div class="item"><div class="thumb" role="img" aria-label="Silver ring" style="background:radial-gradient(#c6c7c9,#111 70%)"></div><div><b>Kelvadro Diamond</b><small>$2,200.00</small></div></div>
    <div class="item"><div class="thumb" role="img" aria-label="Ruby ring on white band" style="background:radial-gradient(#a11a22,#050505 60%)"></div><div><b>Kelvadro Diamond</b><small>$2,200.00</small></div></div>
  </div>
  <div class="list">
    <h4>BEST SELLING</h4>
    <div class="item"><div class="thumb" role="img" aria-label="Gold chains" style="background:linear-gradient(135deg,#6a5a44,#b39c78)"></div><div><b>Kelvadro Diamond</b><small>$2,200.00</small></div></div>
    <div class="item"><div class="thumb" role="img" aria-label="Drop earrings" style="background:linear-gradient(135deg,#5a3a44,#2a6a6a)"></div><div><b>Kelvadro Diamond</b><small>$2,200.00</small></div></div>
    <div class="item"><div class="thumb" role="img" aria-label="Beaded necklace" style="background:linear-gradient(180deg,#1a1a14,#2a8a8a)"></div><div><b>Kelvadro Diamond</b><small>$2,200.00</small></div></div>
    <div class="item"><div class="thumb" role="img" aria-label="Ruby ring" style="background:radial-gradient(#7a2a2a,#111 70%)"></div><div><b>Kelvadro Diamond</b><small>$2,200.00</small></div></div>
    <div class="item"><div class="thumb" role="img" aria-label="Gold pendant" style="background:radial-gradient(#8a1a1a,#8c7a52 55%,#111)"></div><div><b>Kelvadro Diamond</b><small>$2,200.00</small></div></div>
  </div>
  <div class="list">
    <h4>TOP RATED</h4>
    <div class="item"><div class="thumb" role="img" aria-label="Gold ring with red stone" style="background:radial-gradient(#b8481e,#111 70%)"></div><div><b>Kelvadro Diamond</b><small>$2,200.00</small></div></div>
    <div class="item"><div class="thumb" role="img" aria-label="Silver ring" style="background:radial-gradient(#c6c7c9,#111 70%)"></div><div><b>Kelvadro Diamond</b><small>$2,200.00</small></div></div>
    <div class="item"><div class="thumb" role="img" aria-label="Ruby ring on white band" style="background:radial-gradient(#a11a22,#050505 60%)"></div><div><b>Kelvadro Diamond</b><small>$2,200.00</small></div></div>
    <div class="item"><div class="thumb" role="img" aria-label="Gold chains" style="background:linear-gradient(135deg,#6a5a44,#b39c78)"></div><div><b>Kelvadro Diamond</b><small>$2,200.00</small></div></div>
    <div class="item"><div class="thumb" role="img" aria-label="Drop earrings" style="background:linear-gradient(135deg,#5a3a44,#2a6a6a)"></div><div><b>Kelvadro Diamond</b><small>$2,200.00</small></div></div>
  </div>
</section>

<section class="newsletter">
  <div class="copy"><span>Join our Newslette, to Get All Latest Offers</span><b>Discounts and Other Benefits</b></div>
  <div class="field">Enter Your Email Address</div>
  <div class="sub">SUBSCRIBE</div>
</section>

<footer class="footer">
  <div class="col" style="left:112px">
    <div class="logo" style="margin-bottom:18px">KELVADRO</div>
    <p>Lorem ipsum dolor sit amet, consectetur adipisicing elit. Dolorem quaerat, deleniti necessitatibus in magnam eaque temporibus cupiditate alias voluptatibus, beatae a impedit.</p>
    <div class="socials"><span></span><span></span><span></span><span></span></div>
  </div>
  <div class="col" style="left:445px">
    <h5>Quick Link</h5>
    <ul><li>› About Us</li><li>› FAQ</li><li>› Products</li><li>› Offers</li><li>› Reviews</li></ul>
  </div>
  <div class="col" style="left:613px">
    <h5>CATEGORIES</h5>
    <ul><li>› Ring</li><li>› Brcelet</li><li>› Tourmaline</li><li>› Jewellery</li><li>› Diamond And Jewellery</li></ul>
  </div>
  <div class="col" style="left:863px">
    <h5>Contact Info</h5>
    <ul>
      <li><svg width="12" height="12" viewBox="0 0 12 12"><circle cx="6" cy="3.5" r="2.5" fill="#ddd"/><path d="M1 12a5 5 0 0 1 10 0z" fill="#ddd"/></svg>&nbsp; Marcus Ellery</li>
      <li><svg width="12" height="12" viewBox="0 0 24 24"><path d="M6.6 10.8a15 15 0 0 0 6.6 6.6l2.2-2.2a1 1 0 0 1 1-.3 11 11 0 0 0 3.6.6 1 1 0 0 1 1 1V20a1 1 0 0 1-1 1A17 17 0 0 1 3 4a1 1 0 0 1 1-1h3.5a1 1 0 0 1 1 1 11 11 0 0 0 .6 3.6 1 1 0 0 1-.3 1z" fill="#ddd"/></svg>&nbsp; 555-014-2290</li>
      <li><svg width="12" height="10" viewBox="0 0 12 10"><rect width="12" height="10" fill="#ddd"/><path d="M0 0l6 5 6-5" stroke="#0a0b0c" fill="none"/></svg>&nbsp; hello@kelvadro.com</li>
      <li style="width:230px;line-height:22px;height:auto"><svg width="10" height="12" viewBox="0 0 10 14"><path d="M5 0a5 5 0 0 1 5 5c0 4-5 9-5 9S0 9 0 5a5 5 0 0 1 5-5z" fill="#ddd"/></svg>&nbsp; 2280 Harbor Crest Ave, Marlow Bay</li>
    </ul>
  </div>
  <div class="bottom">
    <span>Copyright © 2021 <b>KELVADRO</b> - All rights reserved.</span>
    <div class="links"><span>Privacy policy</span><i></i><span>Terms &amp; conditions</span></div>
  </div>
</footer>

</body>
</html>
```